Redesign Action Graphic For Product Page on Website

Attached is the current version of the graphic that needs redesigning. The graphic will on the page of our site, which doesn't need any of your skills. This page is our photo book sales page.

We offer our photo books in two formats. First, a video version of the book that they can rent. Second, buy a print version of the book.

The graphic should clearly point the user to the option the are most interested in.

Cover of the photo book is required to be part of the graphic.

Preferred file format for design is InDesign.

Thank you for your consideration. Best of luck. Feedback given to finalist.

Page graphic will be on:
http://www.bramblepairs.example/true-pairs-natsuki-sorami/

Reference:
http://www.bramblepairs.example/directory/

```html
<!DOCTYPE html>
<html lang="en">
<head>
<meta charset="utf-8">
<title>True Pairs : Natsuki &amp; Sorami</title>
<link rel="stylesheet" href="https://fonts.googleapis.com/css2?family=Open+Sans:wght@400;600;700&family=Arimo:wght@400&display=swap">
<style>
  :root {
    --page-dark: #1c1c1c;
    --accent-yellow: #f2ef5a;
    --accent-teal: #33c6c0;
    --rule-grey: #8a8a8a;
    --panel-bg: rgba(22, 22, 22, 0.88);
    --text-light: #ffffff;
    --text-muted: #9a9a9a;
    --ad-bg: #e6e6e6;
    --ad-text: #1a1a1a;
    --button-top: #fbfb9a;
    --button-bottom: #e9e61c;
    --video-rental-block: #2a2a2a;
    --print-block: #c8141b;
    --player-bar: #111111;
  }
  * { box-sizing: border-box; margin: 0; padding: 0; }
  html, body { width: 1200px; height: 882px; overflow: hidden; }
  body {
    position: relative;
    font-family: "Open Sans", Arial, sans-serif;
    color: var(--text-light);
    background: var(--page-dark);
  }
  .page-backdrop {
    position: absolute; inset: 0;
    background:
      radial-gradient(ellipse 520px 300px at 330px 260px, #5a5a5a 0%, transparent 70%),
      radial-gradient(ellipse 600px 360px at 1000px 200px, #4d4d4d 0%, transparent 70%),
      radial-gradient(ellipse 500px 300px at 950px 700px, #3f3f3f 0%, transparent 70%),
      linear-gradient(160deg, #333 0%, #1e1e1e 55%, #2b2b2b 100%);
  }
  .abs { position: absolute; }

  .top-rule-brand { left: 258px; top: 7px; width: 155px; height: 2px; background: var(--accent-teal); }
  .top-rule-nav { left: 427px; top: 7px; width: 503px; height: 2px; background: var(--rule-grey); }

  .brand { left: 262px; top: 30px; display: flex; align-items: center; gap: 6px; }
  .brand-mark { width: 14px; height: 14px; background: var(--text-light); }
  .brand-text { display: flex; flex-direction: column; }
  .brand-name { font-size: 12.5px; font-weight: 700; line-height: 13px; color: var(--text-light); }
  .brand-tagline { font-size: 4.5px; font-weight: 700; line-height: 6px; color: var(--text-light); letter-spacing: 0.2px; }

  .main-nav { left: 430px; top: 36px; display: flex; gap: 7px; font-size: 9.5px; font-weight: 400; }
  .main-nav span { color: var(--text-light); }

  .social-links { right: 272px; top: 37px; display: flex; gap: 8px; font-size: 8.5px; font-weight: 600; color: var(--text-muted); }

  .page-title { left: 257px; top: 82px; font-size: 25.5px; font-weight: 400; color: var(--accent-yellow); letter-spacing: 0.1px; }
  .title-rule { left: 258px; top: 123px; width: 670px; height: 1px; background: var(--rule-grey); }

  .post-panel { left: 270px; top: 136px; width: 658px; height: 696px; background: var(--panel-bg); }
  .post-title { left: 278px; top: 140px; font-size: 18px; font-weight: 400; color: var(--accent-yellow); }

  .video-player { left: 278px; top: 177px; width: 640px; height: 360px; background: var(--player-bar); overflow: hidden; }
  .video-frame {
    position: absolute; left: 0; top: 24px; width: 640px; height: 313px;
    background:
      linear-gradient(180deg, #222 0%, #eee 10%, #fafafa 16%, #111 22%, #000 45%, #e4e4e4 55%, #fff 70%, #ddd 85%, #e8c8cc 93%, #999 100%),
      #000;
  }
  .video-frame::after {
    content: ""; position: absolute; inset: 0;
    background: linear-gradient(90deg, rgba(60,60,60,.85) 0%, rgba(0,0,0,0) 30%);
  }
  .video-caption { position: absolute; left: 10px; top: 6px; font-family: Arimo, Arial, sans-serif; font-size: 11px; color: #ddd; }
  .video-top-icons { position: absolute; right: 8px; top: 5px; }
  .play-button { position: absolute; left: 286px; top: 156px; width: 68px; height: 47px; border-radius: 11px; background: rgba(30,30,30,.9); }
  .progress-track { position: absolute; left: 0; top: 331px; width: 640px; height: 4px; background: #555; }
  .progress-knob { position: absolute; left: 3px; top: 329px; width: 9px; height: 9px; border-radius: 50%; background: #ccc; }
  .player-controls { position: absolute; left: 0; top: 337px; width: 640px; height: 23px; background: #1b1b1b; }
  .player-time { position: absolute; left: 74px; top: 5px; font-family: Arimo, Arial, sans-serif; font-size: 9.5px; color: #ddd; }
  .player-time span { color: #888; }
  .player-brand { position: absolute; left: 578px; top: 5px; font-family: Arimo, Arial, sans-serif; font-size: 9px; color: #888; }

  .format-offer { left: 278px; top: 562px; width: 643px; height: 228px; background: radial-gradient(ellipse 260px 200px at 50% 50%, #fff 0%, var(--ad-bg) 100%); overflow: hidden; }
  .partner-block { position: absolute; top: 0; display: flex; align-items: center; justify-content: center; font-size: 14px; font-weight: 600; color: var(--text-light); }
  .partner-block.rental { left: 35px; width: 132px; height: 87px; background: var(--video-rental-block); }
  .partner-block.print { left: 486px; width: 98px; height: 87px; background: var(--print-block); }
  .offer-label { position: absolute; font-family: Arimo, Arial, sans-serif; font-size: 18px; letter-spacing: -0.2px; color: var(--ad-text); white-space: nowrap; }
  .offer-label.rental { left: 14px; top: 121px; }
  .offer-label.print { left: 428px; top: 118px; }
  .offer-button {
    position: absolute; top: 175px; width: 145px; height: 35px;
    display: flex; align-items: center; justify-content: center;
    font-family: Arimo, Arial, sans-serif; font-size: 18.5px; color: var(--ad-text);
    background: linear-gradient(180deg, var(--button-top) 0%, var(--button-bottom) 60%, #dcd80f 100%);
    border: 1px solid #c9c600;
    box-shadow: 2px 3px 3px rgba(0,0,0,.35);
  }
  .offer-button.rental { left: 30px; }
  .offer-button.print { left: 472px; }
  .book-cover {
    position: absolute; left: 254px; top: 2px; width: 146px; height: 222px;
    background: linear-gradient(135deg, #9a9a9a 0%, #3a3a3a 45%, #1a1a1a 65%, #6e6e6e 100%);
    box-shadow: 3px 2px 6px rgba(0,0,0,.4);
  }
  .book-spine { position: absolute; left: 254px; top: 2px; width: 8px; height: 222px; background: linear-gradient(90deg, #111, #555); }

  .reply-link { left: 895px; top: 816px; font-size: 9px; font-weight: 700; color: var(--accent-teal); text-decoration: underline; }

  .footer-rule-left { left: 258px; top: 843px; width: 435px; height: 1px; background: var(--rule-grey); }
  .footer-rule-right { left: 706px; top: 843px; width: 211px; height: 1px; background: var(--rule-grey); }
  .copyright { left: 259px; top: 858px; font-size: 7.5px; color: var(--text-muted); }
  .footer-contact { left: 705px; top: 856px; display: flex; align-items: center; gap: 6px; font-size: 7.5px; color: var(--text-muted); }
</style>
</head>
<body>
  <div class="page-backdrop" role="img" aria-label="Blurred black and white photograph of a couple filling the page background"></div>

  <div class="abs top-rule-brand"></div>
  <div class="abs top-rule-nav"></div>

  <div class="abs brand">
    <span class="brand-mark"></span>
    <span class="brand-text">
      <span class="brand-name">BRAMBLE PAIRS</span>
      <span class="brand-tagline">ENTERTAINMENT FOR PAIRS</span>
    </span>
  </div>

  <nav class="abs main-nav">
    <span>LATEST</span>
    <span>DIRECTORY</span>
  </nav>

  <div class="abs social-links">
    <span>Vidrune</span>
    <span>Skyvarn</span>
    <span>Pallwick</span>
  </div>

  <h1 class="abs page-title">TRUE PAIRS : NATSUKI &amp; SORAMI</h1>
  <div class="abs title-rule"></div>

  <div class="abs post-panel"></div>
  <h2 class="abs post-title">Natsuki &amp; Sorami : Photo Book</h2>

  <div class="abs video-player">
    <div class="video-frame" role="img" aria-label="Motion-blurred still from the photo book trailer"></div>
    <span class="video-caption">trailers draft 8 960x540</span>
    <svg class="video-top-icons" width="36" height="14" viewBox="0 0 36 14">
      <circle cx="3" cy="7" r="2" fill="#fff"/><circle cx="10" cy="3" r="2" fill="#fff"/><circle cx="10" cy="11" r="2" fill="#fff"/>
      <path d="M3 7 L10 3 M3 7 L10 11" stroke="#fff" stroke-width="1.3"/>
      <circle cx="29" cy="7" r="6" fill="#fff"/>
      <rect x="28.2" y="6" width="1.6" height="4.5" fill="#111"/><rect x="28.2" y="3.3" width="1.6" height="1.6" fill="#111"/>
    </svg>
    <div class="play-button">
      <svg width="68" height="47" viewBox="0 0 68 47"><path d="M27 15 L44 23.5 L27 32 Z" fill="#fff"/></svg>
    </div>
    <div class="progress-track"></div>
    <div class="progress-knob"></div>
    <div class="player-controls">
      <svg width="70" height="23" viewBox="0 0 70 23" style="position:absolute;left:0;top:0">
        <path d="M19 6 L29 11.5 L19 17 Z" fill="#bbb"/>
        <path d="M49 9 H52 L56 6 V17 L52 14 H49 Z" fill="#bbb"/>
        <path d="M58 8.5 Q60 11.5 58 14.5" stroke="#bbb" fill="none"/>
      </svg>
      <span class="player-time">0:00 <span>/ 2:32</span></span>
      <svg width="10" height="10" viewBox="0 0 10 10" style="position:absolute;left:557px;top:7px"><circle cx="5" cy="5" r="4.5" fill="#888"/><path d="M5 2.5 V5 H7" stroke="#1b1b1b" fill="none"/></svg>
      <span class="player-brand">Vidrune</span>
      <svg width="16" height="14" viewBox="0 0 16 14" style="position:absolute;left:620px;top:5px"><path d="M1 5V1H5M11 1H15V5M15 9V13H11M5 13H1V9" stroke="#ccc" stroke-width="1.4" fill="none"/></svg>
    </div>
  </div>

  <section class="abs format-offer">
    <div class="partner-block rental">Velmora</div>
    <div class="partner-block print">Inkhollow</div>
    <div class="book-cover" role="img" aria-label="Photo book cover: black and white portrait of the couple with the title Natsuki &amp; Sorami"></div>
    <div class="book-spine"></div>
    <p class="offer-label rental">VIDEO PHOTO BOOK</p>
    <p class="offer-label print">PRINTED PHOTO BOOK</p>
    <span class="offer-button rental">View now</span>
    <span class="offer-button print">Buy now</span>
  </section>

  <span class="abs reply-link">reply</span>

  <div class="abs footer-rule-left"></div>
  <div class="abs footer-rule-right"></div>
  <p class="abs copyright">COPYRIGHT © 2013 - ALL RIGHTS RESERVED</p>
  <div class="abs footer-contact">
    <svg width="12" height="12" viewBox="0 0 12 12"><circle cx="6" cy="6" r="6" fill="#ddd"/><rect x="3" y="4" width="6" height="4.2" fill="#222"/><path d="M3 4 L6 6.4 L9 4" stroke="#ddd" stroke-width=".8" fill="none"/></svg>
    <span>CONTACT@BRAMBLEPAIRS.EXAMPLE</span>
  </div>
</body>
</html>
```